sydney wedding photography business needs a business card design

we need a business card design for a sydney based wedding photography and videography business. our business name is :golden hour photography and video. our target clients are 24-35 yrs female. our style is candid, organic, natural, dynamic. we are a team of young photographers and videographers, and help brides to create memories that they will cherish for the rest of their lives. the logo will be provided. we want an elegant design that reflects our style, and also want to give a great impression to our clients that we are one of the best studios in sydney and our brand means quality and premium service.

Target Market(s)

bride to be, 24-35 years old, living in sydney and surrunding areas

Industry/Entity Type

Wedding Photography

Contact Information for Business Card

address: 57 marrow lane, bexton nsw 2041
mobile: 0431872056
phone: (02) 9361 2748
info@goldenhourstudio.net.au
www.goldenhourstudio.net.au
facebook:goldenhourbridals
instagram:goldenhourbridals

Font styles to use
Serif
Sans Serif

Requirements
Nice to have
• maybe add my slogan"memories beyond eternity" if the layout looks good
Should not have
• no black color, not good idea for wedding biz card

```html
<!DOCTYPE html>
<html lang="en">
<head>
<meta charset="utf-8">
<title>Golden Hour Photography and Video – Business Card</title>
<link rel="stylesheet" href="https://fonts.googleapis.com/css2?family=Roboto:wght@300;400&display=swap">
<style>
  :root {
    --canvas-bg: #e9e6e1;
    --card-front: #1f3149;
    --card-front-deep: #16253a;
    --gold: #d8b13c;
    --ink-light: #f4f4f4;
    --sky-top: #6f93b8;
    --sky-mid: #3f6489;
    --sky-deep: #1d3350;
  }
  * { box-sizing: border-box; margin: 0; padding: 0; }
  html, body {
    width: 1200px; height: 858px; overflow: hidden;
    background: var(--canvas-bg);
    font-family: "Roboto", Helvetica, Arial, sans-serif;
  }
  .canvas {
    width: 1200px; height: 858px;
    display: flex; align-items: center; justify-content: center; gap: 40px;
  }
  .card {
    position: relative;
    width: 540px; height: 309px;
    border-radius: 4px;
    overflow: hidden;
    box-shadow: 0 10px 28px rgba(0,0,0,.22);
  }

  /* Front */
  .card--front {
    background: linear-gradient(160deg, var(--card-front) 0%, var(--card-front-deep) 100%);
  }
  .brand {
    position: absolute;
    color: var(--gold);
    font-weight: 400;
    line-height: 1.05;
  }
  .card--front .brand { left: 34px; top: 196px; }
  .brand__name { font-size: 40px; letter-spacing: .5px; }
  .brand__sub { font-size: 13px; letter-spacing: 6px; text-transform: uppercase; margin-top: 8px; }

  .contacts {
    position: absolute; right: 18px; top: 22px;
    display: flex; gap: 10px;
  }
  .contacts__lines {
    list-style: none;
    text-align: right;
    color: var(--ink-light);
    font-weight: 300;
    font-size: 13px;
  }
  .contacts__lines li { height: 19px; line-height: 19px; white-space: nowrap; }
  .contacts__icons { list-style: none; }
  .contacts__icons li { height: 19px; display: flex; align-items: center; }
  .icon { width: 14px; height: 14px; display: block; }

  /* Back */
  .card--back .photo {
    position: absolute; inset: 0;
    background: linear-gradient(160deg, var(--sky-top) 0%, var(--sky-mid) 45%, var(--sky-deep) 100%);
  }
  .card--back .brand {
    left: 0; right: 0; top: 110px; text-align: center;
  }
</style>
</head>
<body>
<main class="canvas">

  <section class="card card--front" aria-label="Business card front">
    <div class="contacts">
      <ul class="contacts__lines">
        <li>(02) 9361 2748</li>
        <li>0431872056</li>
        <li>www.goldenhourstudio.net.au</li>
        <li>info@goldenhourstudio.net.au</li>
        <li>goldenhourbridals</li>
        <li>goldenhourbridals</li>
        <li>57 marrow lane, bexton nsw 2041</li>
      </ul>
      <ul class="contacts__icons" aria-hidden="true">
        <li><svg class="icon" viewBox="0 0 14 14"><rect width="14" height="14" fill="#d8b13c"/><path d="M4 3.5l1.6-.3.9 2-1 .8a5 5 0 0 0 2.5 2.5l.8-1 2 .9-.3 1.6C7.5 10.3 3.7 6.5 4 3.5z" fill="#1f3149"/></svg></li>
        <li><svg class="icon" viewBox="0 0 14 14"><rect width="14" height="14" fill="#d8b13c"/><rect x="4.5" y="2.5" width="5" height="9" rx="1" fill="#1f3149"/></svg></li>
        <li><svg class="icon" viewBox="0 0 14 14"><rect width="14" height="14" fill="#d8b13c"/><circle cx="7" cy="7" r="3.8" fill="none" stroke="#1f3149" stroke-width="1.1"/><path d="M3.2 7h7.6M7 3.2v7.6" stroke="#1f3149" stroke-width="1"/></svg></li>
        <li><svg class="icon" viewBox="0 0 14 14"><rect width="14" height="14" fill="#d8b13c"/><rect x="3" y="4" width="8" height="6" fill="none" stroke="#1f3149" stroke-width="1.1"/><path d="M3 4l4 3.2L11 4" fill="none" stroke="#1f3149" stroke-width="1.1"/></svg></li>
        <li><svg class="icon" viewBox="0 0 14 14"><rect width="14" height="14" fill="#d8b13c"/></svg></li>
        <li><svg class="icon" viewBox="0 0 14 14"><rect width="14" height="14" fill="#d8b13c"/></svg></li>
        <li><svg class="icon" viewBox="0 0 14 14"><rect width="14" height="14" fill="#d8b13c"/><path d="M7 11.5S4 8.2 4 6a3 3 0 0 1 6 0c0 2.2-3 5.5-3 5.5z" fill="#1f3149"/><circle cx="7" cy="6" r="1" fill="#d8b13c"/></svg></li>
      </ul>
    </div>

    <div class="brand">
      <div class="brand__name">Golden Hour</div>
      <div class="brand__sub">photography and video</div>
    </div>
  </section>

  <section class="card card--back" aria-label="Business card back">
    <div class="photo" role="img" aria-label="Wedding photograph: bride and groom under a white umbrella on a jetty beneath a cloudy blue sky"></div>
    <div class="brand">
      <div class="brand__name">Golden Hour</div>
      <div class="brand__sub">photography and video</div>
    </div>
  </section>

</main>
</body>
</html>
```